New Landing page in Wordpress Design Project

Hi we have launched a new website www.velmorradrapeworks.co.uk and although we are doing a PPC campaign and getting a good number of hits, we are not getting enquiries. I need the website to be adjusted to improve visitor retention and I am lead to believe if your landing page is poor that is the main reason. At the moment the home page is the landing page. I am happy to amend this or add a additional landing page. My own web guru will make the necessary changes. I want to portray a top quality looking site

```html
<!DOCTYPE html>
<html lang="en">
<head>
<meta charset="utf-8">
<title>Velmorra Drapeworks – Home</title>
<link rel="stylesheet" href="https://fonts.googleapis.com/css2?family=Lato:ital,wght@0,300;0,400;0,700;1,300;1,400&family=Source+Sans+3:wght@400;600&display=swap">
<style>
  :root {
    --page-bg: #f8f5dc;
    --accent-orange: #e8906a;
    --deep-navy: #312d40;
    --sea-teal: #4fa79a;
    --brick-red: #c0585a;
    --olive-text: #6b6838;
    --nav-text: #4a4839;
    --brand-teal: #1d7b78;
    --rule: #d9d5bd;
    --arrow-blue: #1a8fd0;
    --white: #ffffff;
  }
  * { box-sizing: border-box; margin: 0; padding: 0; }
  html, body { width: 1200px; height: 1107px; overflow: hidden; background: var(--page-bg); }
  body { font-family: "Source Sans 3", "Helvetica Neue", Arial, sans-serif; color: var(--nav-text); }
  .page { position: relative; width: 1200px; height: 1107px; overflow: hidden; }

  .top-strip { position: absolute; left: 0; top: 0; width: 1200px; height: 6px; background: var(--accent-orange); }

  .brand { position: absolute; left: 45px; top: 24px; display: flex; align-items: center; gap: 10px;
    font-family: "Source Sans 3", sans-serif; font-weight: 600; font-size: 34px; color: var(--brand-teal); letter-spacing: 0.5px; }
  .brand-dot { width: 14px; height: 14px; border-radius: 50%; background: var(--brand-teal); }

  .search { position: absolute; left: 862px; top: 40px; width: 300px; height: 32px; background: var(--white);
    border: 1px solid #dcd9c8; display: flex; align-items: center; padding: 0 8px; font-size: 12.5px; color: #555; }
  .search span { flex: 1; }
  .search svg { width: 16px; height: 16px; }

  .main-nav { position: absolute; left: 44px; top: 107px; width: 1118px; height: 50px; border-bottom: 5px solid var(--accent-orange); }
  .main-nav ul { list-style: none; display: flex; height: 45px; align-items: stretch; }
  .main-nav li { display: flex; align-items: center; font-size: 13.5px; text-transform: uppercase; color: var(--nav-text); margin-right: 28px; }
  .main-nav li.is-active { background: var(--accent-orange); color: var(--white); text-transform: none; font-size: 15px; padding: 0 15px; margin-right: 22px; }

  .hero { position: absolute; left: 43px; top: 167px; width: 1119px; height: 386px;
    background: linear-gradient(90deg, #b8927a 0%, #e8d7b8 22%, #d9e4e2 45%, #c9d8d0 58%, #e4d1b0 75%, #9d6f55 100%); }

  .promo { position: absolute; top: 573px; height: 103px; width: 357px; display: flex; align-items: center; justify-content: center;
    font-family: "Lato", sans-serif; font-weight: 300; color: var(--white); font-size: 27px; letter-spacing: 0.5px; }
  .promo-offers { left: 43px; background: var(--deep-navy); font-weight: 400; }
  .promo-offers em { font-style: italic; font-weight: 300; margin: 0 6px; }
  .promo-delivery { left: 423px; background: var(--sea-teal); }
  .promo-delivery em { font-style: italic; font-weight: 400; margin-right: 7px; }
  .promo-delivery sup { font-size: 10px; vertical-align: 14px; margin-left: 2px; }
  .promo-sale { left: 803px; background: var(--brick-red); justify-content: flex-start; padding-left: 47px; }
  .promo-sale strong { font-weight: 700; margin-right: 8px; }
  .sale-seal { position: absolute; right: 6px; top: 4px; width: 96px; height: 96px; }

  .welcome { position: absolute; left: 40px; top: 702px; width: 1120px; text-align: center; font-size: 23px; line-height: 29px; color: var(--olive-text); }
  .divider { position: absolute; left: 52px; top: 783px; width: 1095px; height: 1px; background: var(--rule); }

  .carousel-arrow { position: absolute; top: 908px; width: 22px; height: 38px; }
  .arrow-prev { left: 48px; }
  .arrow-next { left: 1133px; }
  .product-tile { position: absolute; top: 834px; width: 309px; height: 193px; }
  .tile-sofa { left: 95px; background: linear-gradient(160deg, #c9c3b4 0%, #e4e1d9 45%, #b7b2a6 100%); }
  .tile-fabric { left: 446px; background: linear-gradient(90deg, #4a4742 0%, #8a8578 40%, #b4aa98 70%, #6c5d50 100%); }
  .tile-cushions { left: 799px; background: linear-gradient(135deg, #3a3f3c 0%, #6e6a52 40%, #b59a35 65%, #2f3a3c 100%); }
  .new-badge { position: absolute; left: 355px; top: 818px; width: 66px; height: 66px; border-radius: 50%; background: #1486c4;
    border: 3px solid var(--white); box-shadow: 0 0 0 2px #1486c4; display: flex; align-items: center; justify-content: center;
    font-family: "Lato", sans-serif; color: var(--white); font-size: 19px; }

  .site-footer { position: absolute; left: 43px; top: 1066px; width: 1116px; height: 41px; background: var(--deep-navy); color: var(--white);
    display: flex; align-items: center; justify-content: space-between; padding: 0 12px; font-size: 11.5px; }
</style>
</head>
<body>
<div class="page">
  <div class="top-strip"></div>

  <div class="brand"><span class="brand-dot"></span>Velmorra Drapeworks</div>

  <div class="search">
    <span>Search entire store here...</span>
    <svg viewBox="0 0 16 16" fill="none" stroke="#e8906a" stroke-width="2"><circle cx="6.5" cy="6.5" r="4.5"/><line x1="10" y1="10" x2="14.5" y2="14.5"/></svg>
  </div>

  <nav class="main-nav">
    <ul>
      <li class="is-active">Home</li>
      <li>About Us</li>
      <li>News</li>
      <li>Curtains</li>
      <li>Scatter Cushions &amp; Bed Throws</li>
      <li>Gallery</li>
      <li>Contact Us</li>
      <li>Testimonials</li>
    </ul>
  </nav>

  <div class="hero" role="img" aria-label="Elegant room with cream swag curtains framing a tall window overlooking treetops"></div>

  <div class="promo promo-offers">DISCOUNTS<em>&amp;</em>OFFERS</div>
  <div class="promo promo-delivery"><em>FREE</em>UK DELIVERY<sup>*</sup></div>
  <div class="promo promo-sale"><strong>SALE</strong>NOW ON
    <svg class="sale-seal" viewBox="0 0 96 96">
      <polygon fill="#fff" points="48,2 53,9 60,3 63,11 71,7 72,15 80,13 79,22 87,22 84,30 92,32 87,39 94,43 88,48 94,53 87,57 92,64 84,66 87,74 79,74 80,83 72,81 71,89 63,85 60,93 53,87 48,94 43,87 36,93 33,85 25,89 24,81 16,83 17,74 9,74 12,66 4,64 9,57 2,53 8,48 2,43 9,39 4,32 12,30 9,22 17,22 16,13 24,15 25,7 33,11 36,3 43,9"/>
      <text x="48" y="53" text-anchor="middle" font-family="Lato, sans-serif" font-weight="700" font-size="16" fill="#c0585a">SALE</text>
    </svg>
  </div>

  <p class="welcome">Hi my name is Helena. Velmorra Drapeworks is my inspiration. I’m passionate about my fabrics and take pride in<br>what I do. I’ve always enjoyed creating the WOW factor. Designer curtains have never looked so good!</p>
  <div class="divider"></div>

  <svg class="carousel-arrow arrow-prev" viewBox="0 0 22 38"><polyline points="18,3 5,19 18,35" fill="none" stroke="#1a8fd0" stroke-width="5"/></svg>
  <div class="product-tile tile-sofa" role="img" aria-label="White sofa with colourful striped scatter cushions in a bright room"></div>
  <div class="product-tile tile-fabric" role="img" aria-label="Grey patterned curtain fabric beside dark ceramic vases"></div>
  <div class="product-tile tile-cushions" role="img" aria-label="Ochre, teal and cream cushions with beaded trims"></div>
  <div class="new-badge">NEW</div>
  <svg class="carousel-arrow arrow-next" viewBox="0 0 22 38"><polyline points="4,3 17,19 4,35" fill="none" stroke="#1a8fd0" stroke-width="5"/></svg>

  <footer class="site-footer">
    <span>Home | Sitemap | Terms &amp; Condition</span>
    <span>© 2013 Copyrights Velmorra Drapeworks All Rights Reserved</span>
  </footer>
</div>
</body>
</html>
```